Dale Hornsby's Swingcraft Big Band — Hot & Sticky ------ CD Cover Art (and Disc Art)

Need a front cover jacket and a disc design for a fantastic all-pro big band (jazz/funk/reggae) CD. We really want to use a group photo somehow since so many of the band members are world famous, LA's finest studio musicians with mostly original music arranged by the biggest names in jazz. Playful, fun, lighthearted, tasteful arrangements with world class soloists.

Target Market(s)

Music/Jazz/Big band enthusiasts; other musicians

Other font styles liked:
• See uploaded file #4

Colors

Designer to choose colors to be used in the design.

Requirements
Must have
• Legibility . . . must be easy to read and not crowded or cluttered. Font idea below (A Quiet Night Beneath The Tangled Pines) is for feel and flavor. It is absolutely not necessary to match if you have something you like better.
Nice to have
• Colorful but not tacky. Maybe a play on the CD title, Hot and Sticky?

```html
<!DOCTYPE html>
<html lang="en">
<head>
<meta charset="utf-8">
<title>Dale Hornsby's Swingcraft Big Band — Hot &amp; Sticky</title>
<link rel="stylesheet" href="https://fonts.googleapis.com/css2?family=Bowlby+One&family=Open+Sans:wght@400;700&display=swap">
<style>
  :root {
    --cover-black: #0b0b0b;
    --streak: rgba(255, 255, 255, 0.05);
    --gold: #e8c14a;
    --white: #ffffff;
    --red: #d9394d;
    --photo-border: #f4f1ea;
  }
  * { margin: 0; padding: 0; box-sizing: border-box; }
  html, body {
    width: 1200px;
    height: 1200px;
    overflow: hidden;
    background: var(--cover-black);
  }
  .cover {
    position: relative;
    width: 1200px;
    height: 1200px;
    overflow: hidden;
    background:
      radial-gradient(ellipse 60% 40% at 50% 55%, rgba(255,255,255,0.10), transparent 70%),
      repeating-linear-gradient(90deg, transparent 0 14px, var(--streak) 14px 16px, transparent 16px 37px, rgba(255,255,255,0.03) 37px 40px),
      linear-gradient(180deg, #151515 0%, var(--cover-black) 45%, #101010 100%);
  }
  .title-block {
    position: absolute;
    left: 118px;
    top: 70px;
    font-family: "Bowlby One", "Arial Black", sans-serif;
    line-height: 0.98;
    letter-spacing: 1px;
  }
  .title-block .leader { color: var(--gold); font-size: 80px; display: block; }
  .title-block .band { color: var(--white); font-size: 52px; display: block; margin-top: 6px; }
  .title-block .album { color: var(--red); font-size: 80px; display: block; margin-top: 4px; }

  .band-photo {
    position: absolute;
    left: 92px;
    top: 352px;
    width: 1016px;
    height: 540px;
    border: 7px solid var(--photo-border);
    background:
      linear-gradient(180deg, transparent 62%, rgba(176, 122, 72, 0.85) 78%, #8a5a34 100%),
      linear-gradient(90deg, #3b8a8c 0%, #46606a 25%, #3a2b30 50%, #7a2f4a 78%, #c0504e 100%);
  }

  .tagline {
    position: absolute;
    left: 0;
    right: 0;
    top: 960px;
    text-align: center;
    font-family: "Open Sans", Arial, sans-serif;
    font-size: 46px;
    color: var(--white);
    font-weight: 400;
  }
  .tagline .highlight { color: var(--gold); font-weight: 700; margin-left: 12px; }
</style>
</head>
<body>
  <main class="cover">
    <h1 class="title-block">
      <span class="leader">Dale Hornsby's</span>
      <span class="band">Swingcraft Big Band</span>
      <span class="album">Hot &amp; Sticky</span>
    </h1>
    <div class="band-photo" role="img" aria-label="Group photo of the big band members with their instruments and music stands in a recording studio"></div>
    <p class="tagline">A Quiet Night Beneath<span class="highlight">The Tangled Pines</span></p>
  </main>
</body>
</html>
```